Cloud Storage Homepage Design

We need a redesign of our homepage for www.vextorabin.com. The current homepage is aweful but has most of the information that needs to be presented, so use it for feature reference.

Our website offers customers a cloud storage solution for storing and sharing their files.

We would like the homepage to have a preview, maybe via a screenshot or two that shows new visitors our control panel/file manager and lists our features in a visually pleasing way.

Homepage we like:
www.quillosync.com
www.dunk.com

We would also like a section on the homepage, that shows a mobile phone with a screenshot of the control panel, with text that says "Mobile access and desktop app coming soon" or some text that is similar, but the point is that we are working a mobile version and a desktop application.
Updates

Target Market(s)

Businesses, professionals and consumers with large amounts of digital data.

Industry/Entity Type

Storage

Requirements
Must have
• Must be in same color scheme as the rest of the website. Must be clean. Must show off the control panel and features.

```html
<!DOCTYPE html>
<html lang="en">
<head>
<meta charset="utf-8">
<title>Vextorabin – Cloud Storage</title>
<link href="https://fonts.googleapis.com/css2?family=Signika:wght@400;600&family=Arimo:wght@400;700&display=swap" rel="stylesheet">
<style>
:root{
  --orange:#e8731c;
  --orange-light:#f39a2f;
  --orange-dark:#d35f14;
  --ink:#222;
  --dark:#1b1b1b;
  --text:#555;
  --muted:#777;
  --panel:#f0f0f0;
  --line:#d8d8d8;
  --white:#fff;
}
*{margin:0;padding:0;box-sizing:border-box}
html,body{width:822px;height:1200px;overflow:hidden}
body{position:relative;background:var(--white);font-family:Arimo,Arial,sans-serif;color:var(--text)}
.abs{position:absolute}
.heading{font-family:Signika,Arial,sans-serif}

/* header */
.site-header{left:0;top:0;width:822px;height:45px;background:linear-gradient(#2a2a2a,#111)}
.brand{left:64px;top:11px;display:flex;align-items:center;gap:8px;font-family:Signika,sans-serif;font-weight:600;font-size:19px;color:var(--white)}
.brand-mark{width:16px;height:16px;border-radius:50%;background:var(--orange)}
.main-nav{left:360px;top:0;height:45px;display:flex;align-items:center;font-size:11px;color:#ccc}
.main-nav span{padding:0 13px;border-left:1px solid #3a3a3a}
.main-nav span:first-child{border-left:0;color:var(--white)}
.auth{top:13px;height:19px;padding:0 6px;line-height:19px;background:linear-gradient(var(--orange-light),var(--orange));color:var(--white);font-family:Signika,sans-serif;font-weight:600;font-size:10.5px;border-radius:2px}

/* hero */
.hero{left:0;top:45px;width:822px;height:226px;background:linear-gradient(#f39a33,var(--orange) 60%,#e2681a)}
.hero-title{left:89px;top:78px;font-size:28px;font-weight:600;color:var(--white)}
.hero-text{left:90px;top:116px;width:320px;font-size:10.4px;line-height:17.2px;color:var(--white)}
.upload-btn{left:90px;top:191px;width:192px;height:34px;background:linear-gradient(#2c2c2c,#0d0d0d);border-radius:2px;display:flex;align-items:center;gap:10px;padding-left:20px;color:var(--white);font-family:Signika,sans-serif;font-size:16px}
.slider-dot{top:241px;width:18px;height:18px;border-radius:50%;background:var(--white)}
.hero-art{left:476px;top:78px;width:252px;height:160px;border-radius:60px 60px 12px 12px;background:radial-gradient(circle at 50% 40%,#f6b04d,#e07e23)}

/* benefits */
.benefits{left:0;top:271px;width:822px;height:127px;background:linear-gradient(var(--white),#eeeeee);border-bottom:1px solid var(--line)}
.benefit-divider{top:282px;width:1px;height:115px;background:var(--line)}
.benefit-icon{top:289px;width:30px;height:30px;border-radius:4px}
.benefit-title{top:302px;font-size:17px;font-weight:600;color:var(--orange-dark)}
.benefit-text{top:335px;width:196px;font-size:9.4px;line-height:15.8px;text-align:justify;color:#666}

/* mobile */
.device-art{left:96px;top:430px;width:228px;height:158px;border-radius:6px;background:linear-gradient(135deg,#444,#111 60%,#888)}
.mobile-title{left:356px;top:428px;font-size:17px;font-weight:600;color:var(--orange-dark)}
.mobile-text{left:356px;top:461px;width:376px;font-size:9.5px;line-height:15.7px;text-align:justify;color:#666}
.rule{left:62px;top:618px;width:699px;height:1px;background:var(--line)}

/* plans */
.plans-title{left:0;top:634px;width:822px;text-align:center;font-size:17px;color:#888}
.plan{top:672px;width:225px}
.plan-head{height:35px;background:linear-gradient(#4a4a4a,#1f1f1f);color:var(--white);font-family:Signika,sans-serif;font-weight:600;font-size:14px;line-height:35px;text-align:center}
.plan-row{height:42px;margin-top:1.6px;background:var(--panel);border:1px solid #e2e2e2;display:flex;align-items:center;padding-left:25px;gap:9px;font-family:Signika,sans-serif;font-size:12.5px;color:#444}
.plan-row b{font-weight:600;color:#222}
.plan-btn{top:940px;width:116px;height:26px;background:linear-gradient(var(--orange-light),var(--orange));color:var(--white);font-family:Signika,sans-serif;font-weight:600;font-size:12.5px;line-height:26px;text-align:center;border-radius:2px}

/* footer */
.site-footer{left:0;top:991px;width:822px;height:166px;background:#f3f3f3;border-top:2px solid #e2e2e2}
.footer-title{top:1005px;font-size:12px;color:#333}
.link-col{top:1032px;list-style:none;font-size:8.6px;line-height:20px;color:#777}
.link-col li::before{content:"• ";color:#aaa}
.footer-divider{left:580px;top:1004px;width:1px;height:140px;background:var(--line)}
.social{left:620px;display:flex;align-items:center;gap:16px;font-size:8.6px;color:#777}
.social i{width:18px;height:18px;border-radius:2px;display:block}
.social em{font-style:normal;font-size:10px;color:#1f5fa6}
.copyright-bar{left:0;top:1157px;width:822px;height:43px;background:#262626;color:#aaa;font-size:8.6px;text-align:center;line-height:43px}
</style>
</head>
<body>

<header class="site-header abs"></header>
<div class="brand abs"><span class="brand-mark"></span>Vextorabin</div>
<nav class="main-nav abs"><span>Home</span><span>About</span><span>Services</span><span>Sharing</span><span>Help</span></nav>
<div class="auth abs" style="left:652px">REGISTER</div>
<div class="auth abs" style="left:715px">LOG IN</div>

<section class="hero abs"></section>
<h1 class="hero-title heading abs">Fast, Easy and Secure</h1>
<p class="hero-text abs">Vextorabin cloud storage is the perfect solution to quickly and easily store, share and manage your files. Your files are stored at multiple locations for better redundancy. All files types are accepted and we even take care of encoding your video files!</p>
<div class="upload-btn abs">
  <svg width="34" height="22" viewBox="0 0 34 22"><path d="M8 21a7 7 0 0 1 0-14 9 9 0 0 1 17 1 6.5 6.5 0 0 1 1 13z" fill="#fff"/><path d="M17 19V10m-4 4 4-4 4 4" stroke="#e8731c" stroke-width="2.5" fill="none"/></svg>
  Upload Files Now
</div>
<div class="slider-dot abs" style="left:90px"><svg width="18" height="18"><path d="M11 5 6 9l5 4z" fill="#333"/></svg></div>
<div class="slider-dot abs" style="left:111px"><svg width="18" height="18"><path d="M7 5l5 4-5 4z" fill="#333"/></svg></div>
<div class="hero-art abs" role="img" aria-label="Cloud illustration with three document file icons"></div>

<section class="benefits abs"></section>
<div class="benefit-divider abs" style="left:290px"></div>
<div class="benefit-divider abs" style="left:538px"></div>

<div class="benefit-icon abs" style="left:64px;background:#f0b88a" role="img" aria-label="Thumbs up icon"></div>
<h3 class="benefit-title heading abs" style="left:114px">Secured Service</h3>
<p class="benefit-text abs" style="left:67px">Morbi elit arcu, rhoncus eget nisl in, tempor luctus mi. Duis rhoncus nibh nec risus ultrices, ac tincidunt augue scelerisque.</p>

<div class="benefit-icon abs" style="left:318px;background:#666" role="img" aria-label="Settings gear icon"></div>
<h3 class="benefit-title heading abs" style="left:363px">Easy Customizing</h3>
<p class="benefit-text abs" style="left:318px">Morbi elit arcu, rhoncus eget nisl in, tempor luctus mi. Duis rhoncus nibh nec risus ultrices, ac tincidunt augue scelerisque.</p>

<div class="benefit-icon abs" style="left:566px;border-radius:50%;background:#f2c418" role="img" aria-label="Gold coin icon"></div>
<h3 class="benefit-title heading abs" style="left:600px">Affordable Price</h3>
<p class="benefit-text abs" style="left:568px">Morbi elit arcu, rhoncus eget nisl in, tempor luctus mi. Duis rhoncus nibh nec risus ultrices, ac tincidunt augue scelerisque.</p>

<div class="device-art abs" role="img" aria-label="Desktop monitor and mobile phone showing the file manager control panel"></div>
<h2 class="mobile-title heading abs">Mobile access and desktop app coming soon</h2>
<div class="mobile-text abs">
  <p>Duis euismod turpis rutrum, varius ante vitae, pharetra est. Suspendisse tincidunt sapien nec interdum sagittis. Aliquam eleifend libero non congue placerat. Duis dapibus, leo vitae condimentum mattis, diam nulla malesuada tellus, id mollis lorem ligula quis leo. Aenean sollicitudin ullamcorper pulvinar. Phasellus accumsan, orci non tempus tempus, justo urna rutrum metus, sed tempor risus dolor quis dolor.</p>
  <p style="margin-top:6px">Aenean varius viverra dignissim. Duis vitae lacus accumsan, varius dolor nec, convallis tellus. Sed nisi sapien, placerat a semper ut, hendrerit eget felis.</p>
</div>
<div class="rule abs"></div>

<h2 class="plans-title heading abs">Vextorabin Features</h2>

<div class="plan abs" style="left:156px">
  <div class="plan-head">GUEST ACCOUNT FEATURES</div>
  <div class="plan-row"><svg width="13" height="13" viewBox="0 0 13 13"><circle cx="6.5" cy="6.5" r="5.3" fill="none" stroke="#555" stroke-width="1.4"/><path d="M3.8 6.6 6 8.8l5.5-6" fill="none" stroke="#555" stroke-width="1.6"/></svg>Download Speed : <b>Unlimited</b></div>
  <div class="plan-row"><svg width="13" height="13" viewBox="0 0 13 13"><circle cx="6.5" cy="6.5" r="5.3" fill="none" stroke="#555" stroke-width="1.4"/><path d="M3.8 6.6 6 8.8l5.5-6" fill="none" stroke="#555" stroke-width="1.6"/></svg>Upload Speed : <b>Unlimited</b></div>
  <div class="plan-row"><svg width="13" height="13" viewBox="0 0 13 13"><circle cx="6.5" cy="6.5" r="5.3" fill="none" stroke="#555" stroke-width="1.4"/><path d="M3.8 6.6 6 8.8l5.5-6" fill="none" stroke="#555" stroke-width="1.6"/></svg>Filesize Limit : <b>1 GB</b></div>
  <div class="plan-row"><svg width="13" height="13" viewBox="0 0 13 13"><circle cx="6.5" cy="6.5" r="5.3" fill="none" stroke="#555" stroke-width="1.4"/><path d="M3.8 6.6 6 8.8l5.5-6" fill="none" stroke="#555" stroke-width="1.6"/></svg>Storage Limit : <b>1 GB</b></div>
  <div class="plan-row"><svg width="13" height="13" viewBox="0 0 13 13"><circle cx="6.5" cy="6.5" r="5.3" fill="none" stroke="#555" stroke-width="1.4"/><path d="M3.8 6.6 6 8.8l5.5-6" fill="none" stroke="#555" stroke-width="1.6"/></svg>File Manager : <b>Limited</b></div>
</div>
<div class="plan abs" style="left:442px">
  <div class="plan-head">FREE ACCOUNT FEATURES:</div>
  <div class="plan-row"><svg width="13" height="13" viewBox="0 0 13 13"><circle cx="6.5" cy="6.5" r="5.3" fill="none" stroke="#555" stroke-width="1.4"/><path d="M3.8 6.6 6 8.8l5.5-6" fill="none" stroke="#555" stroke-width="1.6"/></svg>Download Speed : <b>Unlimited</b></div>
  <div class="plan-row"><svg width="13" height="13" viewBox="0 0 13 13"><circle cx="6.5" cy="6.5" r="5.3" fill="none" stroke="#555" stroke-width="1.4"/><path d="M3.8 6.6 6 8.8l5.5-6" fill="none" stroke="#555" stroke-width="1.6"/></svg>Upload Speed : <b>Unlimited</b></div>
  <div class="plan-row"><svg width="13" height="13" viewBox="0 0 13 13"><circle cx="6.5" cy="6.5" r="5.3" fill="none" stroke="#555" stroke-width="1.4"/><path d="M3.8 6.6 6 8.8l5.5-6" fill="none" stroke="#555" stroke-width="1.6"/></svg>Filesize Limit : <b>5 GB</b></div>
  <div class="plan-row"><svg width="13" height="13" viewBox="0 0 13 13"><circle cx="6.5" cy="6.5" r="5.3" fill="none" stroke="#555" stroke-width="1.4"/><path d="M3.8 6.6 6 8.8l5.5-6" fill="none" stroke="#555" stroke-width="1.6"/></svg>Storage Limit : <b>100 GB</b></div>
  <div class="plan-row"><svg width="13" height="13" viewBox="0 0 13 13"><circle cx="6.5" cy="6.5" r="5.3" fill="none" stroke="#555" stroke-width="1.4"/><path d="M3.8 6.6 6 8.8l5.5-6" fill="none" stroke="#555" stroke-width="1.6"/></svg>File Manager : <b>Full Featured</b></div>
</div>
<div class="plan-btn abs" style="left:210px">REGISTER NOW</div>
<div class="plan-btn abs" style="left:497px">LOGIN NOW</div>

<footer class="site-footer abs"></footer>
<h4 class="footer-title abs" style="left:63px;font-weight:400">Quick Links</h4>
<ul class="link-col abs" style="left:64px"><li>Integer lobortis</li><li>Curabitur ac</li><li>Phasellus tellus nisl</li><li>Aenean fringilla</li><li>Vestibulum</li><li>Aliquam commodo</li></ul>
<ul class="link-col abs" style="left:196px"><li>Integer lobortis</li><li>Curabitur ac</li><li>Phasellus tellus nisl</li><li>Aenean fringilla</li><li>Vestibulum</li><li>Aliquam commodo</li></ul>
<ul class="link-col abs" style="left:327px"><li>Integer lobortis</li><li>Curabitur ac</li><li>Phasellus tellus nisl</li><li>Aenean fringilla</li><li>Vestibulum</li><li>Aliquam commodo</li></ul>
<ul class="link-col abs" style="left:459px"><li>Integer lobortis</li><li>Curabitur ac</li><li>Phasellus tellus nisl</li><li>Aenean fringilla</li><li>Vestibulum</li><li>Aliquam commodo</li></ul>
<div class="footer-divider abs"></div>
<h4 class="footer-title abs" style="left:620px;font-weight:400">Connect with us</h4>
<div class="social abs" style="top:1035px"><i style="background:#3b5a98"></i><span>Join with us on <em>Friendloop</em></span></div>
<div class="social abs" style="top:1064px"><i style="background:#3fb0e0"></i><span>Follow us on <em style="color:#2a9fd6">Chirpline</em></span></div>
<div class="social abs" style="top:1092px"><i style="background:#1a6fa3"></i><span>Share on <em>Workweave</em></span></div>
<div class="social abs" style="top:1121px"><i style="background:#c9302c"></i><span>Watch on <em style="color:#222">Clipstream</em></span></div>
<div class="copyright-bar abs">Copyright © 2013 Vextorabin. All rights reserved.</div>

</body>
</html>
```